PowerPoint Design Project

We are looking for a corporate presentation design (example content provided on approximately 30 slides).

The design will be a corporate design for our brand: VRAN
Continental Travel Planners Guild
For brand colours, requirements and logo look at: www.vran-guild.example/media
or check the attached documents. We need to incorporate logo and brand but we are happy to refresh the palette. Attached please also find designs and colour palette of our new website-presentation should complement these.

You are also free to use photos from events some of which can be found here:
http://www.socialnet.example/pages/Continental-Travel-Planners-Guild/402915736480193?sk=photos_stream

Most important:
-PROFESSIONAL AUDIENCE-PROFESSIONAL DESIGN
-SIMPLE (see example our homepage in attachment)
-ADDED SIMPLE ANIMATIONS

-DESIGN TO BE DONE ON THE EXAMPLE PRESENTATION BUT TO BE RE-USABLE FOR OTHER PRESENTATIONS
Updates

Hi, we have just uploaded our corporate social media icons which could be added on contact/end slide and on the welcome slide.

Hi all, 

-I uploaded a new high res version of the map which can be included in your designs (feel free to change colour scheme)
-Also amended upload of the Plexo + social media icon

Reason: I am looking forward to seeing a couple more designs. Please try including some suggested animations.

Target Market(s)

Presentation will be B2B and most audience are representatives of various companies in the tourism industry (tour operators, tourist boards, hotels )

Industry/Entity Type

Events

Requirements
Must have
• sleek graphics design
Nice to have
• animations

```html
<!DOCTYPE html>
<html lang="en">
<head>
<meta charset="utf-8">
<title>VRAN — Project Slide</title>
<link rel="stylesheet" href="https://fonts.googleapis.com/css2?family=Open+Sans:wght@400&family=Roboto+Condensed:wght@700&display=swap">
<style>
  :root {
    --navy: #0e1438;
    --navy-edge: #b9bcc8;
    --title-blue: #1f2a7a;
    --bullet-blue: #3b40c4;
    --body-grey: #555a60;
    --list-grey: #4d5257;
    --page-ink: #1a1a1a;
    --copyright: #a4a8ff;
    --paper: #ffffff;
    --mist: #e9e9ec;
    --brand-ink: #ffffff;
  }
  * { margin: 0; padding: 0; box-sizing: border-box; }
  html, body { width: 1200px; height: 900px; overflow: hidden; background: var(--paper); }
  .slide {
    position: relative;
    width: 1200px;
    height: 900px;
    overflow: hidden;
    font-family: "Open Sans", "Segoe UI", sans-serif;
    background:
      radial-gradient(ellipse 900px 600px at 15% 15%, var(--mist) 0%, rgba(233,233,236,0) 70%),
      linear-gradient(160deg, #f1f1f3 0%, #f8f8f9 45%, var(--paper) 80%);
  }
  .texture {
    position: absolute; left: 0; top: 42px; width: 1200px; height: 776px;
    background: linear-gradient(150deg, #f0f0f2 0%, #fafafb 50%, var(--paper) 100%);
    opacity: 0.6;
  }
  .top-band {
    position: absolute; left: 0; top: 0; width: 1200px; height: 42px;
    background: var(--navy);
  }
  .brand-banner { position: absolute; left: 900px; top: 0; width: 270px; height: 390px; }
  .brand-name {
    position: absolute; left: 907px; top: 122px; width: 255px;
    text-align: center;
    font-size: 38px; font-weight: 400; letter-spacing: 2px;
    color: var(--brand-ink);
  }
  .project-title {
    position: absolute; left: 57px; top: 110px;
    font-size: 40px; font-weight: 400;
    color: var(--title-blue);
  }
  .intro {
    position: absolute; left: 55px; top: 189px; width: 820px;
    font-size: 21.5px; line-height: 37.5px;
    color: var(--body-grey);
  }
  .points {
    position: absolute; left: 70px; top: 378px;
    list-style: none;
  }
  .points li {
    position: relative;
    height: 61.5px;
    padding-left: 47px;
    font-size: 28px; line-height: 42px;
    color: var(--list-grey);
  }
  .points li::before {
    content: "»";
    position: absolute; left: 0; top: -2px;
    font-size: 28px;
    color: var(--bullet-blue);
  }
  .foot-band { position: absolute; left: 0; top: 810px; width: 1200px; height: 90px; }
  .page-number {
    position: absolute; left: 36px; top: 841px;
    font-family: "Roboto Condensed", "Arial Narrow", sans-serif;
    font-weight: 700; font-size: 24px;
    color: var(--page-ink);
  }
  .copyright {
    position: absolute; right: 42px; top: 848px;
    font-size: 22px;
    color: var(--copyright);
  }
</style>
</head>
<body>
<div class="slide">
  <div class="texture" role="img" aria-label="Soft silver wave texture"></div>

  <div class="top-band"></div>

  <svg class="brand-banner" viewBox="900 0 270 390" aria-hidden="true">
    <polygon points="911,0 1166,0 1166,304 911,384" fill="var(--navy-edge)"/>
    <polygon points="907,0 1162,0 1162,300 907,380" fill="var(--navy)"/>
  </svg>
  <div class="brand-name">VRAN</div>

  <h1 class="project-title">Project Title Here</h1>
  <p class="intro">Lorem ipsum dolor sit ipsum Lorem ipsum dolor sit ipsum Lorem ipsum dolor sit ipsum Lorem ipsum dolor sit ipsum Lorem ipsum dolor sit ipsum Lorem ipsum Lorem ipsum dolor sit ipsum Lorem ipsum dolor sit ipsum Lorem ipsum dolor sit ipsum</p>

  <ul class="points">
    <li>Lorem ipsum dolor sit ipsum</li>
    <li>Lorem ipsum dolor sit ipsum</li>
    <li>Lorem ipsum dolor sit ipsum</li>
    <li>Lorem ipsum dolor sit ipsum</li>
    <li>Lorem ipsum dolor sit ipsum</li>
  </ul>

  <svg class="foot-band" viewBox="0 810 1200 90" aria-hidden="true">
    <path d="M147 900 L 212 840 Q 238 818 285 818 L 1200 818 L 1200 900 Z" fill="var(--navy)"/>
  </svg>
  <div class="page-number">Page : 02</div>
  <div class="copyright">Copyright text here</div>
</div>
</body>
</html>
```